Business cards need a revamp and change of address. I have included files of current card which has been used for 5 years. Also a photo of my new store fitout which uses a lot of colour and features inspired by cusco Peru. I would like to see design options with and without the butterfly although I do use the butterfly on my current street signage.
Updates

Reason: would like to see more designers submit

Target Market(s)

women 35 - 65

Industry/Entity Type

Business

Contact Information for Business Card

Larkvale Andean Silver Jewellery & Giftware

Requirements
Must have
• logo frontside
• backside the following text:
• Larkvale Jewellery is hand made using the highest quality 950 Peruvian Silver which is purer than 925 Sterling Silver. Larkvale's range of unique, handcrafted products are directly sourced from fair trade producer co-operatives, individual artisans and artisan groups from Peru, South America.
• Phone 02 43168272
• 7/118 Pelham Road Windsor NSW 2754
• Email : sales@larkvale.com.au
Nice to have
• Like us on face book

```html
<!DOCTYPE html>
<html lang="en">
<head>
<meta charset="utf-8">
<title>Larkvale Business Card – Front and Back</title>
<link rel="stylesheet" href="https://fonts.googleapis.com/css2?family=Dosis:wght@400;500;600&display=swap">
<style>
  :root {
    --backdrop: #ece9e4;
    --card: #ffffff;
    --ink: #1b1b1b;
    --muted: #2c2c2c;
    --accent-blue: #1d62c9;
    --butterfly-blue: #1e8fe0;
    --butterfly-deep: #0d4f9e;
    --photo-store: #2f5f86;
    --photo-store-light: #8eb3cf;
    --photo-street: #c9b9a0;
    --photo-street-sky: #a9c3dc;
    --social-square: #3b5a9a;
    --shadow: rgba(0, 0, 0, 0.18);
  }
  * { box-sizing: border-box; margin: 0; padding: 0; }
  html, body {
    width: 1200px; height: 712px; overflow: hidden;
    background: var(--backdrop);
    font-family: "Dosis", "Helvetica Neue", Arial, sans-serif;
    color: var(--ink);
  }
  .stage {
    position: relative; width: 1200px; height: 712px;
    display: flex; align-items: center; justify-content: center; gap: 40px;
  }
  .card {
    position: relative; width: 540px; height: 310px;
    background: var(--card);
    box-shadow: 0 6px 18px var(--shadow);
  }

  /* Front */
  .front-logo {
    position: absolute; left: 110px; top: 105px;
    display: flex; align-items: center; gap: 14px;
  }
  .front-logo .brand-dot {
    width: 22px; height: 22px; border-radius: 50%; background: var(--ink);
  }
  .front-logo .brand-name {
    font-size: 64px; font-weight: 600; letter-spacing: 1px; color: var(--ink); line-height: 1;
  }
  .front-butterfly {
    position: absolute; left: 372px; top: 34px; width: 120px; height: 86px;
    border-radius: 40% 40% 45% 45%;
    background: radial-gradient(ellipse at 50% 45%, var(--butterfly-blue) 0%, var(--butterfly-deep) 80%);
  }
  .front-url {
    position: absolute; right: 30px; bottom: 26px;
    font-size: 15px; font-weight: 500; color: var(--muted); letter-spacing: 0.3px;
  }

  /* Back */
  .back-heading {
    position: absolute; left: 30px; top: 30px;
    font-size: 30px; font-weight: 500; color: var(--accent-blue); line-height: 1;
  }
  .back-about {
    position: absolute; left: 30px; top: 74px; width: 290px;
    font-size: 10.5px; line-height: 1.35; color: var(--muted);
  }
  .back-photo {
    position: absolute; top: 22px; width: 100px; height: 98px;
  }
  .back-photo.store {
    left: 318px;
    background: linear-gradient(160deg, var(--photo-store-light) 0%, var(--photo-store) 55%, #1c3550 100%);
  }
  .back-photo.street {
    left: 428px;
    background: linear-gradient(180deg, var(--photo-street-sky) 0%, var(--photo-street-sky) 30%, var(--photo-street) 60%, #8e7b63 100%);
  }
  .back-logo {
    position: absolute; right: 30px; top: 190px;
    display: flex; align-items: center; gap: 8px;
  }
  .back-logo .brand-dot {
    width: 12px; height: 12px; border-radius: 50%; background: var(--ink);
  }
  .back-logo .brand-name {
    font-size: 36px; font-weight: 600; color: var(--ink); line-height: 1;
  }
  .contact-list {
    position: absolute; left: 30px; top: 196px; list-style: none;
  }
  .contact-list li {
    display: flex; align-items: center; gap: 7px;
    font-size: 11.5px; color: var(--muted); line-height: 1; margin-bottom: 5px;
  }
  .contact-list li.phone { font-size: 19px; margin-bottom: 9px; }
  .contact-list svg { width: 13px; height: 13px; flex: none; }
  .contact-list li.phone svg { width: 17px; height: 17px; }
  .social-square { width: 11px; height: 11px; background: var(--social-square); border-radius: 2px; flex: none; margin: 0 1px; }
</style>
</head>
<body>
<main class="stage">

  <section class="card card-front" aria-label="Business card front">
    <div class="front-logo">
      <span class="brand-dot"></span>
      <span class="brand-name">larkvale</span>
    </div>
    <div class="front-butterfly" role="img" aria-label="Blue morpho butterfly illustration"></div>
    <p class="front-url">www.larkvale.com.au</p>
  </section>

  <section class="card card-back" aria-label="Business card back">
    <h1 class="back-heading">Peruvian Silver</h1>
    <p class="back-about">Larkvale Jewellery is hand made using the highest quality 950 Peruvian Silver which is purer than 925 Sterling Silver. Larkvale's range of unique, handcrafted products are directly sourced from fair trade producer co-operatives, individual artisans and artisan groups from Peru, South America.</p>

    <div class="back-photo store" role="img" aria-label="Photo of the store interior with blue walls and glass display cabinets"></div>
    <div class="back-photo street" role="img" aria-label="Photo of a whitewashed colonial street in Cusco under a cloudy sky"></div>

    <div class="back-logo">
      <span class="brand-dot"></span>
      <span class="brand-name">larkvale</span>
    </div>

    <ul class="contact-list">
      <li class="phone">
        <svg viewBox="0 0 24 24" aria-hidden="true"><path fill="#1b1b1b" d="M6.6 10.8c1.4 2.8 3.8 5.1 6.6 6.6l2.2-2.2c.3-.3.7-.4 1-.2 1.1.4 2.3.6 3.6.6.6 0 1 .4 1 1V20c0 .6-.4 1-1 1C10.6 21 3 13.4 3 4c0-.6.4-1 1-1h3.5c.6 0 1 .4 1 1 0 1.3.2 2.5.6 3.6.1.3 0 .7-.2 1z"/></svg>
        02 43168272
      </li>
      <li>
        <svg viewBox="0 0 24 24" aria-hidden="true"><path fill="none" stroke="#1b1b1b" stroke-width="2" d="M12 21s-6-6.2-6-11a6 6 0 0 1 12 0c0 4.8-6 11-6 11z"/><circle cx="12" cy="10" r="2.2" fill="#1b1b1b"/></svg>
        7/118 Pelham Road Windsor NSW 2754
      </li>
      <li>
        <svg viewBox="0 0 24 24" aria-hidden="true"><rect x="3" y="6" width="18" height="12" fill="none" stroke="#1b1b1b" stroke-width="2"/><path d="M3 6l9 7 9-7" fill="none" stroke="#1b1b1b" stroke-width="2"/></svg>
        sales@larkvale.com.au
      </li>
      <li>
        <svg viewBox="0 0 24 24" aria-hidden="true"><circle cx="12" cy="12" r="9" fill="none" stroke="#1b1b1b" stroke-width="2"/><path d="M3 12h18M12 3c3 3 3 15 0 18M12 3c-3 3-3 15 0 18" fill="none" stroke="#1b1b1b" stroke-width="1.5"/></svg>
        www.larkvale.com.au
      </li>
      <li>
        <span class="social-square"></span>
        Like us
      </li>
    </ul>
  </section>

</main>
</body>
</html>
```